4 Month Comparison Sales Promotion Infographic

HI ALL - SEEMS TO BE SOME CONFUSION RE: JANUARY - JANUARY HAS NO EXTRA BENEFITS, SAME AS DECEMBER. THE DIFFERENCE BETWEEN DECEMBER AND JANUARY IS ONLY PRICE. THE ONLY MONTHS WITH EXTRA BENEFITS ARE OCTOBER AND NOVEMBER. THANK YOU!

Project needs to be completed in 24 hours. Need it for tomorrow by 3pm EST.

Project Overview: We are developing an infographic to effectively present our U.S. Federal Contracting consulting package. This package is currently available for $21,000, despite its components having a retail value of $35,750. Beginning January 1st, 2025, the package price will rise by 25% to $28,600.

Goal of the Project: The primary objective is to motivate customers to purchase the package in October or November, before the upcoming price increase. This infographic will strategically illustrate the incremental value gained from making an earlier purchase.

Target Audience: The focus is on U.S. business owners who typically postpone significant investments during the holiday season, from November 15th to January 1st. The infographic is designed to encourage these customers to consider the benefits of acting sooner rather than later.

Visual Concept: The infographic will employ a "compare/contrast" style to demonstrate the following:

October: Best Value — Achieve the highest total package value of $50,750 at the lowest cost of $21,000.
November: Great Value — Still substantial, with a package value of $41,600 available for the same cost of $21,000.
December: Really Good Value — Standard retail value of $35,750 obtainable for $21,000.
January: Good Deal — Same retail value of $35,750, but at the increased price of $28,600. NO ADDITIONAL BENEFITS (SAME AS DECEMBER)
Key Features:

Clear and compelling visuals that contrast cost versus value for each month.
Design that aligns with your brand’s visual identity, enhancing message delivery through an engaging, on-brand presentation.
A strong emphasis on the superior value of purchasing in October or November over January to highlight the financial wisdom in early decision-making.

This is all displayed in images that we've shared, along with the associated benefits.

Branding Information
Website: www.tarvelmoor.com
Colors:
Primary Color: #042756 (Dark Blue)
Accent Color: #D96F1F (Orange)
Fonts:
Heading Font:
Font Family: Manrope
Font Size: 68px
Line Height: 74.8px
Text Alignment: Left (Start)
Letter Spacing: -1.36px
Body Font:
Font Family: Manrope
Font Size: 18px
Line Height: 32.4px
Letter Spacing: -0.36px

Target Market(s)

Business owners interested in federal contracting

Industry/Entity Type

B2B, but focused on B2B (Business to Government)

Font styles to use
Other font styles liked:
• Manrope (Heading and Body)

Colors
0054AA
0677BA
7BADD7
CADEEF
E8F1F8
EE7325
F08F49
F5BC92
FAE3D3
FDF4ED

Requirements
Must have
• Need to clearly represent the 4 month window, costs, and benefits and difference in cost vs. value. Clearly defined information that highlights value of purchasing in October vs. waiting for later months.
Nice to have
• Unique icons and/or designs that are outside the box and really wow the client.

```html
<!DOCTYPE html>
<html lang="en">
<head>
<meta charset="utf-8">
<title>End of Year Promotion – Tarvelmoor</title>
<link href="https://fonts.googleapis.com/css2?family=Rubik:wght@300;400;500;600;700&display=swap" rel="stylesheet">
<style>
:root{
  --navy:#072552;
  --ink:#0d2a57;
  --label:#4a4f5c;
  --teal:#129f83;
  --yellow:#f1c62c;
  --blue:#5566f2;
  --orange:#f78f48;
  --accent:#d96f1f;
  --cross:#f08a4b;
  --band:#f1f1f1;
  --white:#ffffff;
  --star:#f5c127;
}
*{margin:0;padding:0;box-sizing:border-box}
html,body{width:1200px;height:979px;overflow:hidden}
body{background:var(--navy);font-family:"Rubik",sans-serif;position:relative;color:var(--label)}
.title{position:absolute;top:64px;left:0;width:1200px;text-align:center;color:var(--white);font-weight:500;font-size:53px;letter-spacing:-1px;line-height:1}
.title .hl{color:var(--accent)}

.offer-tag{position:absolute;top:174px;width:162px;display:flex;justify-content:center;align-items:center;gap:6px}
.offer-tag .big{font-size:26px;font-weight:500;line-height:1}
.offer-tag .small{font-size:9.5px;font-weight:500;color:var(--white);line-height:11.5px}

.features{position:absolute;left:126px;top:211px;width:263px;height:646px;background:var(--white);border-radius:19px}
.brand{height:112.6px;position:relative}
.brand-name{position:absolute;left:31px;top:36px;font-size:31px;font-weight:500;color:var(--ink);letter-spacing:-0.3px}
.brand-rule{position:absolute;left:25px;right:39px;bottom:15px;border-top:1px solid #b9bcc4}

.rows{display:grid;grid-template-rows:repeat(8,24.8px) 55px 40px 22px 37px 34px 56px 23px 24px 44px}
.features .rows > div{padding-left:25px;font-size:11.3px;line-height:12.5px;font-weight:300;color:var(--label);display:flex;flex-direction:column;justify-content:center}
.sub{display:grid;grid-template-columns:115px 80px;font-size:6.6px;line-height:12px;margin-top:2px;color:#4a5060}
.sub span::before{content:"• ";color:var(--teal)}

.plan{position:absolute;top:211px;width:162px;height:646px;background:var(--white);border-radius:16px;overflow:hidden}
.plan-head{height:96px;position:relative;color:var(--white)}
.month{position:absolute;left:5px;right:5px;top:5px;height:27px;background:var(--white);border-radius:8px;color:var(--ink);font-size:21px;font-weight:400;text-align:center;line-height:27px;letter-spacing:0.2px}
.cost-label,.value-label{position:absolute;top:52px;font-size:11px;letter-spacing:2.2px;font-weight:400}
.cost-label{left:11px}
.value-label{right:5px;top:54px}
.cost{position:absolute;left:8px;top:65px;font-size:19.5px;font-weight:500}
.value{position:absolute;right:6px;top:69px;font-size:14px;font-weight:500}
.plan .rows{margin-top:16.6px}
.plan .rows > div{display:flex;align-items:center;justify-content:center;font-size:11.2px;color:var(--label);font-weight:300}
.rows > div:nth-child(even){background:var(--band)}
.features .rows > div:nth-child(even){background:none}
.tick{width:18px;height:14px}
.tick path{stroke:var(--teal);stroke-width:3;fill:none}
.cross{width:12px;height:12px}
.cross path{stroke:var(--cross);stroke-width:2.6;fill:none}
.mini{display:grid;grid-template-columns:auto auto;column-gap:14px;font-size:7px;line-height:10.5px;font-weight:300}
.mini span::before{content:"• "}

.oct .plan-head{background:var(--teal)}
.nov .plan-head{background:var(--yellow)}
.dec .plan-head{background:var(--blue)}
.jan .plan-head{background:var(--orange)}

.rating{position:absolute;top:872px;width:180px;text-align:center;color:var(--white)}
.rating .name{font-size:18px;font-weight:400;line-height:22px}
.rating svg{display:block;margin:6px auto 0}
</style>
</head>
<body>
<svg width="0" height="0" style="position:absolute">
  <defs>
    <symbol id="star" viewBox="0 0 20 20"><polygon points="10,1 12.6,7.2 19.3,7.4 14,11.6 15.9,18.2 10,14.4 4.1,18.2 6,11.6 0.7,7.4 7.4,7.2"/></symbol>
    <linearGradient id="half"><stop offset="50%" stop-color="#f5c127"/><stop offset="50%" stop-color="#ffffff"/></linearGradient>
    <symbol id="tk" viewBox="0 0 18 14"><path d="M2 7l5 5L16 2" fill="none" stroke="#129f83" stroke-width="3"/></symbol>
    <symbol id="xx" viewBox="0 0 12 12"><path d="M1 1l10 10M11 1L1 11" fill="none" stroke="#f08a4b" stroke-width="2.6"/></symbol>
  </defs>
</svg>

<h1 class="title">END OF YEAR <span class="hl">PROMOTION</span></h1>

<div class="offer-tag" style="left:398px"><span class="big" style="color:var(--teal)">FREE</span><span class="small">ADDITIONAL<br>BENEFITS</span></div>
<div class="offer-tag" style="left:569px"><span class="big" style="color:var(--yellow)">FREE</span><span class="small">ADDITIONAL<br>BENEFITS</span></div>
<div class="offer-tag" style="left:740px"><span class="big" style="color:var(--blue)">NO</span><span class="small">ADDITIONAL<br>BENEFITS</span></div>
<div class="offer-tag" style="left:911px"><span class="big" style="color:var(--orange)">NO</span><span class="small">ADDITIONAL<br>BENEFITS</span></div>

<section class="features">
  <div class="brand"><div class="brand-name">Tarvelmoor</div><div class="brand-rule"></div></div>
  <div class="rows">
    <div>Vendor Registry Optimization</div>
    <div>Micromarket Optimization</div>
    <div>Capability Statement</div>
    <div>Capabilities Briefing Deck</div>
    <div>Capabilities Tri-Fold Brochure</div>
    <div>Sources Sought Response Template</div>
    <div>Market Research &amp; Intelligence Report</div>
    <div>Pipeline Scan Report</div>
    <div>30 Days of Comprehensive Biz Dev
      <div class="sub"><span>Daily Solicitation Matching</span><span>Solicitation Review</span><span>Agency Briefing Appt. Setting</span><span>Proposal Writing</span></div></div>
    <div>Daily Solicitation Matching<br>Through Jan 31st</div>
    <div>Solicitation Review &amp; Proposal Writing</div>
    <div>Capability Statement Design for<br>Opp Specific Requirements</div>
    <div>Capability Statement<br>Customization (Opp Specific)</div>
    <div>E-Mail Templates
      <div class="sub" style="grid-template-columns:75px 80px;line-height:10.5px;margin-left:4px"><span>Subcontract</span><span>Mentor/Protege</span><span>Teaming</span><span>Debriefing</span><span>Joint Venture</span><span>Sources Sought</span></div></div>
    <div>Federal Biz Dev Coaching Session</div>
    <div>List of CO POC's</div>
    <div>List of Targeted Primes w/<br>contact information</div>
  </div>
</section>

<section class="plan oct" style="left:398px">
  <div class="plan-head"><div class="month">OCTOBER</div><span class="cost-label">COST</span><span class="value-label">VALUE</span><span class="cost">$21,000</span><span class="value">$50,750</span></div>
  <div class="rows">
    <div><svg class="tick"><use href="#tk"/></svg></div>
    <div><svg class="tick"><use href="#tk"/></svg></div>
    <div><svg class="tick"><use href="#tk"/></svg></div>
    <div><svg class="tick"><use href="#tk"/></svg></div>
    <div><svg class="tick"><use href="#tk"/></svg></div>
    <div><svg class="tick"><use href="#tk"/></svg></div>
    <div><svg class="tick"><use href="#tk"/></svg></div>
    <div><svg class="tick"><use href="#tk"/></svg></div>
    <div><svg class="tick"><use href="#tk"/></svg></div>
    <div>4 months</div>
    <div>15 additional</div>
    <div>1 additional</div>
    <div>15 hours</div>
    <div><div class="mini"><span>Subcontract</span><span>Mentor/Protege</span><span>Teaming</span><span>Debriefing</span><span>Joint Venture</span><span>Sources Sought</span></div></div>
    <div>4</div>
    <div>Top 100</div>
    <div>Top 50</div>
  </div>
</section>

<section class="plan nov" style="left:569px">
  <div class="plan-head"><div class="month">NOVEMBER</div><span class="cost-label">COST</span><span class="value-label">VALUE</span><span class="cost">$21,000</span><span class="value">$41,600</span></div>
  <div class="rows">
    <div><svg class="tick"><use href="#tk"/></svg></div>
    <div><svg class="tick"><use href="#tk"/></svg></div>
    <div><svg class="tick"><use href="#tk"/></svg></div>
    <div><svg class="tick"><use href="#tk"/></svg></div>
    <div><svg class="tick"><use href="#tk"/></svg></div>
    <div><svg class="tick"><use href="#tk"/></svg></div>
    <div><svg class="tick"><use href="#tk"/></svg></div>
    <div><svg class="tick"><use href="#tk"/></svg></div>
    <div><svg class="tick"><use href="#tk"/></svg></div>
    <div>3 months</div>
    <div>5 additional</div>
    <div>1 additional</div>
    <div>5 hours</div>
    <div><div class="mini" style="grid-template-columns:auto"><span>Subcontract</span><span>Teaming</span></div></div>
    <div>4</div>
    <div>Top 10</div>
    <div>Top 10</div>
  </div>
</section>

<section class="plan dec" style="left:740px">
  <div class="plan-head"><div class="month">DECEMBER</div><span class="cost-label">COST</span><span class="value-label">VALUE</span><span class="cost">$21,000</span><span class="value">$35,750</span></div>
  <div class="rows">
    <div><svg class="tick"><use href="#tk"/></svg></div>
    <div><svg class="tick"><use href="#tk"/></svg></div>
    <div><svg class="tick"><use href="#tk"/></svg></div>
    <div><svg class="tick"><use href="#tk"/></svg></div>
    <div><svg class="tick"><use href="#tk"/></svg></div>
    <div><svg class="tick"><use href="#tk"/></svg></div>
    <div><svg class="tick"><use href="#tk"/></svg></div>
    <div><svg class="tick"><use href="#tk"/></svg></div>
    <div><svg class="tick"><use href="#tk"/></svg></div>
    <div><svg class="cross"><use href="#xx"/></svg></div>
    <div><svg class="cross"><use href="#xx"/></svg></div>
    <div><svg class="cross"><use href="#xx"/></svg></div>
    <div><svg class="cross"><use href="#xx"/></svg></div>
    <div><svg class="cross"><use href="#xx"/></svg></div>
    <div><svg class="cross"><use href="#xx"/></svg></div>
    <div><svg class="cross"><use href="#xx"/></svg></div>
    <div><svg class="cross"><use href="#xx"/></svg></div>
  </div>
</section>

<section class="plan jan" style="left:911px">
  <div class="plan-head"><div class="month">JANUARY</div><span class="cost-label">COST</span><span class="value-label">VALUE</span><span class="cost">$28,650</span><span class="value">$35,750</span></div>
  <div class="rows">
    <div><svg class="tick"><use href="#tk"/></svg></div>
    <div><svg class="tick"><use href="#tk"/></svg></div>
    <div><svg class="tick"><use href="#tk"/></svg></div>
    <div><svg class="tick"><use href="#tk"/></svg></div>
    <div><svg class="tick"><use href="#tk"/></svg></div>
    <div><svg class="tick"><use href="#tk"/></svg></div>
    <div><svg class="tick"><use href="#tk"/></svg></div>
    <div><svg class="tick"><use href="#tk"/></svg></div>
    <div><svg class="tick"><use href="#tk"/></svg></div>
    <div><svg class="cross"><use href="#xx"/></svg></div>
    <div><svg class="cross"><use href="#xx"/></svg></div>
    <div><svg class="cross"><use href="#xx"/></svg></div>
    <div><svg class="cross"><use href="#xx"/></svg></div>
    <div><svg class="cross"><use href="#xx"/></svg></div>
    <div><svg class="cross"><use href="#xx"/></svg></div>
    <div><svg class="cross"><use href="#xx"/></svg></div>
    <div><svg class="cross"><use href="#xx"/></svg></div>
  </div>
</section>

<div class="rating" style="left:386px"><div class="name">Best Value</div>
  <svg width="120" height="20" viewBox="0 0 120 20"><g fill="var(--star)"><use href="#star" x="0" width="20" height="20"/><use href="#star" x="25" width="20" height="20"/><use href="#star" x="50" width="20" height="20"/><use href="#star" x="75" width="20" height="20"/><use href="#star" x="100" width="20" height="20"/></g></svg></div>
<div class="rating" style="left:561px"><div class="name">Great Value</div>
  <svg width="120" height="20" viewBox="0 0 120 20"><g fill="var(--star)"><use href="#star" x="0" width="20" height="20"/><use href="#star" x="25" width="20" height="20"/><use href="#star" x="50" width="20" height="20"/><use href="#star" x="75" width="20" height="20"/></g><use href="#star" x="100" width="20" height="20" fill="url(#half)"/></svg></div>
<div class="rating" style="left:733px"><div class="name">Really Great Value</div>
  <svg width="120" height="20" viewBox="0 0 120 20"><g fill="var(--star)"><use href="#star" x="0" width="20" height="20"/><use href="#star" x="25" width="20" height="20"/><use href="#star" x="50" width="20" height="20"/><use href="#star" x="75" width="20" height="20"/></g><use href="#star" x="100" width="20" height="20" fill="#fff"/></svg></div>
<div class="rating" style="left:897px"><div class="name">Good Deal</div>
  <svg width="120" height="20" viewBox="0 0 120 20"><g fill="var(--star)"><use href="#star" x="0" width="20" height="20"/><use href="#star" x="25" width="20" height="20"/><use href="#star" x="50" width="20" height="20"/></g><use href="#star" x="75" width="20" height="20" fill="url(#half)"/><use href="#star" x="100" width="20" height="20" fill="#fff"/></svg></div>
</body>
</html>
```